Non profit housing agency needs a brochure design

We need a brochure design for our non profit housing organization, 'TAVOL, Inc.' The message we would like to communicate is: "We Have A Place You Can Call Home". Our agency provides housing for the homeless and at-risk. In the brochure, we want to tell the public about our 3 agency programs.
1. The BRIDGE (Builders Reaching Into Daily Growth) Program- for homeless adult men ex-offenders
2. Marla's Garden- for homeless adult women ex-offenders and their children
3. Delphine's Harbor- for domestic minor victims of sex trafficking
TAVOL, Inc. is a housing organization that serves various populations in the above programs. Attached is our newly designed logo from a talented Artmingle designer. We would like to build on this design using the same colors and creativity.
Target Market(s)
Government, churches, public
Industry/Entity Type
Non Profit
Look and feel

```html
<!DOCTYPE html>
<html lang="en">
<head>
<meta charset="utf-8">
<title>TAVOL, Inc. — Brochure</title>
<link rel="stylesheet" href="https://fonts.googleapis.com/css2?family=Ultra&family=Roboto+Slab:wght@400;700&family=Noticia+Text:ital@1&display=swap">
<style>
  :root {
    --navy: #27306e;
    --gold: #fbb817;
    --headline-gold: #fdc21f;
    --orange: #f0922b;
    --white: #ffffff;
    --shadow: rgba(0, 0, 0, 0.18);
  }
  * { box-sizing: border-box; margin: 0; padding: 0; }
  html, body { width: 850px; height: 1200px; overflow: hidden; background: var(--white); }
  .brochure { position: relative; width: 850px; height: 1200px; background: var(--white); font-family: "Roboto Slab", serif; }

  .brand { position: absolute; top: 86px; left: 0; width: 850px; text-align: center;
    font-family: "Roboto Slab", serif; font-weight: 400; font-size: 46px; color: var(--orange); letter-spacing: 1px; }

  .rule-double { position: absolute; left: 0; width: 850px; height: 3px; background: var(--gold); }
  .rule-double.upper { top: 178px; }
  .rule-double.lower { top: 185px; }
  .rule-dotted { position: absolute; left: 0; width: 850px; border-top: 4px dotted var(--navy); }
  .rule-dotted.top { top: 193px; }
  .rule-dotted.middle { top: 626px; }
  .rule-dotted.bottom { top: 1070px; }

  .headline { position: absolute; top: 298px; left: 30px; width: 380px; text-align: center;
    font-family: "Ultra", serif; color: var(--headline-gold); text-shadow: 2px 2px 0 var(--shadow); line-height: 1.2; }
  .headline .line { display: block; font-size: 33px; }
  .headline .line.big { font-size: 60px; line-height: 1.05; }

  .house-art { position: absolute; left: 392px; top: 217px; width: 411px; height: 387px; }

  .section-title { position: absolute; left: 47px; top: 660px; font-family: "Ultra", serif; color: var(--navy); line-height: 1; }
  .section-title .small { display: block; font-size: 32px; }
  .section-title .large { display: block; font-size: 44px; margin-top: 2px; }

  .programs { position: absolute; left: 47px; top: 760px; width: 751px; height: 291px;
    background: var(--gold); box-shadow: 4px 4px 0 rgba(0,0,0,0.12); list-style: none; padding: 62px 0 0 57px; }
  .programs::before { content: ""; position: absolute; top: -20px; left: 354px;
    border-left: 20px solid transparent; border-right: 20px solid transparent; border-bottom: 20px solid var(--gold); }
  .program { margin-bottom: 8px; color: var(--white); }
  .program-name { font-family: "Roboto Slab", serif; font-weight: 700; font-size: 20px; line-height: 28px; }
  .program-audience { font-family: "Noticia Text", serif; font-style: italic; font-size: 19px; line-height: 26px; padding-left: 23px; }

  .contact { position: absolute; left: 0; top: 1088px; width: 850px; height: 112px; background: var(--gold);
    text-align: center; padding-top: 15px; font-family: "Roboto Slab", serif; font-size: 21px; color: var(--navy); line-height: 25.5px; }
</style>
</head>
<body>
<main class="brochure">
  <header class="brand">TAVOL, Inc.</header>
  <div class="rule-double upper"></div>
  <div class="rule-double lower"></div>
  <div class="rule-dotted top"></div>

  <h1 class="headline">
    <span class="line">"WE HAVE A PLACE</span>
    <span class="line">YOU CAN CALL</span>
    <span class="line big">HOME"</span>
  </h1>

  <svg class="house-art" role="img" aria-label="Illustration of a small tan house with a blue roof and red base" viewBox="0 0 411 387">
    <defs>
      <linearGradient id="houseTone" x1="0" y1="0" x2="0" y2="1">
        <stop offset="0" stop-color="#3b6cc0"/>
        <stop offset="0.45" stop-color="#e2b86a"/>
        <stop offset="1" stop-color="#8e1c1c"/>
      </linearGradient>
    </defs>
    <rect width="411" height="387" rx="10" fill="url(#houseTone)" opacity="0.85"/>
  </svg>

  <div class="rule-dotted middle"></div>

  <h2 class="section-title">
    <span class="small">OUR</span>
    <span class="large">PROGRAMS</span>
  </h2>

  <ol class="programs">
    <li class="program">
      <div class="program-name">1. The BRIDGE (Builders Reaching Into Daily Growth) Program</div>
      <div class="program-audience">for homeless adult men ex-offenders</div>
    </li>
    <li class="program">
      <div class="program-name">2. Marla's Garden</div>
      <div class="program-audience">for homeless adult women ex-offenders and their children</div>
    </li>
    <li class="program">
      <div class="program-name">3. Delphine's Harbor</div>
      <div class="program-audience">for domestic minor victims of sex trafficking</div>
    </li>
  </ol>

  <div class="rule-dotted bottom"></div>

  <footer class="contact">
    <div>+1 555 014 2290</div>
    <div>www.tavolhomes.org</div>
    <div>info@tavolhomes.org</div>
  </footer>
</main>
</body>
</html>
```